Fifty Turning Pages

- Title: FIFTY TURNING PAGES
- Subtitle: 50 Years • 50 Songs • A Lifetime of Memories
- Content: 50 songs (year + artist) listed between 1976–2024 - see attached file for song listing
- Personal dedication: “For the woman who remembers life one song at a time. Happy 50th Birthday — January 2025. With love, Harold.”
- Final size: A2 (420 × 594 mm)
- Style: Elegant, music-themed, typography-led (minimal graphic elements like vinyl / soundwave / gold line accents).
- Deliverables: High-resolution A2 PDF (print-ready), plus source file (Canva/PSD/AI).
- Color preference: Matte palette (black/white/cream/gold accents).
- Target: Framed print quality poster.

```html
<!DOCTYPE html>
<html lang="en">
<head>
<meta charset="utf-8">
<title>Fifty Turning Pages</title>
<link href="https://fonts.googleapis.com/css2?family=Crimson+Text:wght@400;600;700&family=Cormorant+Garamond:wght@400;500&family=Great+Vibes&display=swap" rel="stylesheet">
<style>
  :root{
    --paper:#ffffff;
    --ink:#1d1b19;
    --gold:#b8944f;
    --line:#8a8783;
  }
  html,body{margin:0;padding:0;overflow:hidden;background:var(--paper);}
  .poster{position:relative;width:849px;height:1200px;background:var(--paper);color:var(--ink);overflow:hidden;}
  .note{position:absolute;left:50%;transform:translateX(-50%);width:20px;height:32px;fill:var(--gold);}
  .note--top{top:22px;}
  .note--mid{top:728px;}
  .tracklist{position:absolute;top:130px;left:0;width:849px;display:flex;font-family:"Crimson Text",serif;font-size:17px;line-height:22.5px;}
  .tracklist__col{list-style:none;margin:0;padding:0;}
  .tracklist__col--early{width:413px;text-align:right;}
  .tracklist__col--late{margin-left:12px;text-align:left;}
  .tracklist__year{font-weight:700;}
  .title{position:absolute;left:196px;top:778px;width:464px;height:230px;margin:0;font-weight:400;}
  .title__top{position:absolute;left:0;top:0;width:464px;text-align:center;font-family:"Cormorant Garamond",serif;font-weight:500;font-size:52px;letter-spacing:1px;line-height:1;white-space:nowrap;}
  .staff{position:absolute;left:0;top:62px;width:464px;height:100px;}
  .staff line{stroke:var(--line);stroke-width:1;}
  .title__main{position:absolute;left:0;top:38px;width:464px;text-align:center;font-family:"Cormorant Garamond",serif;font-weight:400;font-size:142px;line-height:1;letter-spacing:2px;color:var(--gold);transform:scaleY(1.3);transform-origin:top center;}
  .subtitle{position:absolute;left:196px;top:1008px;width:464px;margin:0;text-align:center;font-family:"Crimson Text",serif;font-weight:600;font-size:15px;letter-spacing:0.6px;color:var(--ink);text-transform:uppercase;white-space:nowrap;}
  .dedication{position:absolute;left:212px;top:1042px;margin:0;font-family:"Great Vibes",cursive;font-size:26px;line-height:30px;color:var(--ink);}
  .dedication__sign{display:block;padding-left:260px;}
</style>
</head>
<body>
<main class="poster">
  <svg class="note note--top" viewBox="0 0 14 22" aria-hidden="true"><ellipse cx="4.5" cy="18" rx="4.5" ry="3.4"/><rect x="7.6" y="1" width="1.4" height="17"/><path d="M9 1c1 4 5 5 4 10-.5-3-2-5-4-5z"/></svg>

  <section class="tracklist" aria-label="Fifty songs by year">
    <ul class="tracklist__col tracklist__col--early">
      <li>Dolly Marston - <span class="tracklist__year">1976</span></li>
      <li>Melvin Hale - <span class="tracklist__year">1977</span></li>
      <li>Tasha Quinn - <span class="tracklist__year">1978</span></li>
      <li>Marcus Jansen - <span class="tracklist__year">1979</span></li>
      <li>Delia Rhodes - <span class="tracklist__year">1980</span></li>
      <li>Lucas Vandermeer - <span class="tracklist__year">1981</span></li>
      <li>Stanley Warder - <span class="tracklist__year">1982</span></li>
      <li>Leon Ritchfield - <span class="tracklist__year">1983</span></li>
      <li>Pulse-R.K.D. - <span class="tracklist__year">1984</span></li>
      <li>LaMarque - <span class="tracklist__year">1985</span></li>
      <li>Winona Hastings - <span class="tracklist__year">1986</span></li>
      <li>LaVane - <span class="tracklist__year">1987</span></li>
      <li>Benny Braxley - <span class="tracklist__year">1988</span></li>
      <li>Heart II Heart - <span class="tracklist__year">1989</span></li>
      <li>Bly Cole DeVane - <span class="tracklist__year">1990</span></li>
      <li>Janelle Jameson - <span class="tracklist__year">1991</span></li>
      <li>KDM - <span class="tracklist__year">1992</span></li>
      <li>RNV - <span class="tracklist__year">1993</span></li>
      <li>Amariah - <span class="tracklist__year">1994</span></li>
      <li>Marla J. Bright - <span class="tracklist__year">1995</span></li>
      <li>Bluecourt - <span class="tracklist__year">1996</span></li>
      <li>Maisie Ellery - <span class="tracklist__year">1997</span></li>
      <li>Lorna Ridge - <span class="tracklist__year">1998</span></li>
      <li>Serenity's Crew - <span class="tracklist__year">1999</span></li>
    </ul>
    <ul class="tracklist__col tracklist__col--late">
      <li><span class="tracklist__year">2000</span> – D'Amarco</li>
      <li><span class="tracklist__year">2001</span> – Alina Keaton</li>
      <li><span class="tracklist__year">2002</span> – Nello</li>
      <li><span class="tracklist__year">2003</span> – Belicé</li>
      <li><span class="tracklist__year">2004</span> – Archer</li>
      <li><span class="tracklist__year">2005</span> – Kamden Weir</li>
      <li><span class="tracklist__year">2006</span> – Ro-Ve</li>
      <li><span class="tracklist__year">2007</span> – Rianelle</li>
      <li><span class="tracklist__year">2008</span> – Lil Dane</li>
      <li><span class="tracklist__year">2009</span> – Kay-V &amp; Alina Keaton</li>
      <li><span class="tracklist__year">2010</span> – Drayton</li>
      <li><span class="tracklist__year">2011</span> – Kelsey Rowan</li>
      <li><span class="tracklist__year">2012</span> – Rianelle</li>
      <li><span class="tracklist__year">2013</span> – Jason Timberline ft. KAY-V</li>
      <li><span class="tracklist__year">2014</span> – Farrell Wilkins</li>
      <li><span class="tracklist__year">2015</span> – The Midweek</li>
      <li><span class="tracklist__year">2016</span> – Drayton, Wisefox &amp; Kyra</li>
      <li><span class="tracklist__year">2017</span> – Darnell Cezar &amp; S.H.E.</li>
      <li><span class="tracklist__year">2018</span> – Pete Malloy ft. 22 Valiant</li>
      <li><span class="tracklist__year">2019</span> – Kahleel</li>
      <li><span class="tracklist__year">2020</span> – Jon Ledger ft. Jenae Aiyo</li>
      <li><span class="tracklist__year">2021</span> – Brennan Marsh</li>
      <li><span class="tracklist__year">2022</span> – ZEA</li>
      <li><span class="tracklist__year">2023</span> – Tiva</li>
      <li><span class="tracklist__year">2024</span> – Kenric Lamont ft. ZEA</li>
    </ul>
  </section>

  <svg class="note note--mid" viewBox="0 0 14 22" aria-hidden="true"><ellipse cx="4.5" cy="18" rx="4.5" ry="3.4"/><rect x="7.6" y="1" width="1.4" height="17"/><path d="M9 1c1 4 5 5 4 10-.5-3-2-5-4-5z"/></svg>

  <h1 class="title">
    <span class="title__top">FIFTY TURNING</span>
    <svg class="staff" viewBox="0 0 464 100" aria-hidden="true">
      <line x1="0" y1="2" x2="464" y2="2"/>
      <line x1="0" y1="26" x2="464" y2="26"/>
      <line x1="0" y1="50" x2="464" y2="50"/>
      <line x1="0" y1="74" x2="464" y2="74"/>
      <line x1="0" y1="98" x2="464" y2="98"/>
    </svg>
    <span class="title__main">PAGES</span>
  </h1>

  <p class="subtitle">50 Years • 50 Songs • A Lifetime of Memories</p>

  <p class="dedication">For the woman who remembers life<br>one song at a time.<br>Happy 50th Birthday — January 2025.<span class="dedication__sign">-Harold</span></p>
</main>
</body>
</html>
```